Office and banking equipment supplier needs a company profile/products catalogue

we need a profile/products catalog design for our company. we are specialized in banking and office related equipment. we have an old design but we need a new refined one. I'm attaching the old one (a higher resolution one can be sent through we transfer) where the products' images are up to date, yet the design is no convincing. the new catalog should have a noticeable identity, properly executed and descriptive with minimal text. the old one is quite big but it has all of the products listed in it. with a description of each category. however, the designer is free to add, amend or delete whatever he/she thinks suitable to grab the attention of the reader.

Target Market(s)

Banks, Education sectors, Office Automation, Government

Industry/Entity Type

Office Furniture

Font styles to use
Serif

Requirements
Must have
• lifetime design, excellent point of entry, eye catching design that directs the customer towards the product, intergartion
Nice to have
• Catalog copy must be clear, concise, easy to read, educational or even entertaining. The catalog user must be teased to ask about more information required to make a purchase decision, or risk losing the sale. Ordering information and pricing should be presented in easy to read tables.
• it must be visual, allowing the user to breeze through with minimal effort. Photography supports the visual experience.
• a good info graphic about the company.
Should not have
• dull designs.

```html
<!DOCTYPE html>
<html lang="en">
<head>
<meta charset="utf-8">
<title>Meridian Office Systems – Company Profile Cover</title>
<link rel="stylesheet" href="https://fonts.googleapis.com/css2?family=Roboto:wght@400&family=PT+Serif:wght@700&family=Amiri:wght@700&display=swap">
<style>
  :root {
    --backdrop: #d9d9d9;
    --royal-blue: #2f44a6;
    --royal-blue-deep: #22328a;
    --silver: #b3b5b9;
    --silver-light: #d4d5d8;
    --charcoal: #262626;
    --white: #ffffff;
    --text-dark: #222222;
  }
  * { margin: 0; padding: 0; box-sizing: border-box; }
  html, body { width: 1200px; height: 678px; overflow: hidden; }
  body { background: var(--backdrop); position: relative; font-family: "Roboto", sans-serif; }

  .spread {
    position: absolute; left: 100px; top: 89px;
    width: 1000px; height: 500px;
    display: flex;
    box-shadow: 0 6px 18px rgba(0,0,0,.18);
  }
  .page { position: relative; width: 500px; height: 500px; overflow: hidden; }

  /* back cover */
  .back-cover {
    background: linear-gradient(135deg, var(--royal-blue) 0%, var(--royal-blue-deep) 100%);
  }
  .back-cover .top-band {
    position: absolute; left: 0; top: 0; width: 100%; height: 75px;
    background: linear-gradient(180deg, var(--silver-light), var(--silver));
  }
  .bottom-band {
    position: absolute; left: 0; bottom: 0; width: 100%; height: 90px;
    background: var(--charcoal);
  }
  .web-address {
    position: absolute; bottom: 28px;
    color: var(--white); font-size: 13px; letter-spacing: .3px;
  }
  .back-cover .web-address { left: 60px; }
  .brand-mark {
    position: absolute; display: flex; align-items: center; gap: 10px;
    color: var(--white); font-family: "PT Serif", serif; font-weight: 700;
    white-space: nowrap;
  }
  .brand-mark .dot {
    width: 18px; height: 18px; border-radius: 50%; background: var(--white);
  }
  .back-cover .brand-mark { left: 165px; top: 200px; font-size: 34px; }

  /* front cover */
  .front-cover { background: var(--silver); }
  .front-cover svg { position: absolute; inset: 0; }
  .cover-label {
    position: absolute; left: 22px; top: 38px;
    font-size: 13px; color: var(--text-dark);
  }
  .front-cover .brand-mark { left: 22px; top: 222px; font-size: 28px; gap: 8px; }
  .front-cover .brand-mark .dot { width: 16px; height: 16px; }
  .company-name {
    position: absolute; left: 22px; top: 292px; width: 165px;
    color: var(--white); font-family: "PT Serif", serif; font-weight: 700;
    font-size: 10px; line-height: 1.3; text-transform: uppercase;
  }
  .company-name-ar {
    position: absolute; left: 22px; top: 326px; width: 180px;
    color: var(--white); font-family: "Amiri", serif; font-weight: 700;
    font-size: 12px; direction: rtl; text-align: left; white-space: nowrap;
  }
  .front-cover .web-address { left: 150px; }
</style>
</head>
<body>
  <main class="spread">
    <section class="page back-cover">
      <div class="top-band"></div>
      <div class="brand-mark"><span class="dot"></span>Meridian</div>
      <div class="bottom-band"></div>
      <p class="web-address">www.meridian-os.jo</p>
    </section>

    <section class="page front-cover">
      <svg width="500" height="500" viewBox="0 0 500 500">
        <defs>
          <linearGradient id="silver-fade" x1="0" y1="0" x2="0" y2="1">
            <stop offset="0" stop-color="#d4d5d8"/>
            <stop offset="1" stop-color="#b3b5b9"/>
          </linearGradient>
          <linearGradient id="coin-photo" x1="0" y1="0" x2="1" y2="1">
            <stop offset="0" stop-color="#d6a46a"/>
            <stop offset=".55" stop-color="#a06a3c"/>
            <stop offset="1" stop-color="#3b2a1f"/>
          </linearGradient>
        </defs>
        <rect class="top-area" width="500" height="410" fill="url(#silver-fade)"/>
        <polygon class="blue-wedge" points="0,75 140,75 240,410 0,410" fill="#2f44a6"/>
        <polygon class="photo-frame" points="148,86 500,60 500,410 246,410" fill="#ffffff"/>
        <polygon class="cover-photo" role="img" aria-label="Close-up photo of stacked copper and silver coins on a table"
                 points="160,94 500,70 500,410 258,410" fill="url(#coin-photo)"/>
        <rect class="bottom-band" y="410" width="500" height="90" fill="#262626"/>
      </svg>
      <p class="cover-label">Company Profile</p>
      <div class="brand-mark"><span class="dot"></span>Meridian</div>
      <p class="company-name">Meridian Office Systems<br>Co. Ltd.</p>
      <p class="company-name-ar">شركة ميريديان للأنظمة المكتبية المحدودة</p>
      <p class="web-address">www.meridian-os.jo</p>
    </section>
  </main>
</body>
</html>
```